Artistic Poster for a Short Film

I am the Writer/Director of an upcoming short film called "Driftwater" and I need a 20x30 poster for the project screening. The screening is coming up very soon so apologies for the quick turnaround time. Here is a short synopsis:

"Walter is a mysterious man who is lost and disoriented. With the help of Marisol, he searches for items out of an old diary written long ago by a woman named Gloria, despite not understanding exactly why he does so. Marisol helps, but when they are unsuccessful she confronts Walter: Does he know why he restlessly searches for these items? The truth is shocking, and reveals Walter's connections to Marisol, Gloria, and the strange old diary.

The truth is that Walter is actually an old man, and Marisol is his caretaker and granddaughter. His memories, including those of Gloria, his deceased wife, have been destroyed by Dementia. He often wakes believing himself to be at an earlier stage of his life, and therefore meets many of the challenges of life with anger and confusion."

Here is the film's website: http://www.driftwater-film.example
Here is our successful Fundbarrow: http://www.fundbarrow.example/projects/502847719/driftwater-a-short-film

The design should be dark and simple. I'm a fan of the art-prints that this short film used (scroll down to see): http://www.fundbarrow.example/projects/ruthvanderlo/kettle-a-short-film-based-on-the-story-by-omar-quill but I'm also open to other ideas. If you google "alternative movie posters" you'll see what I mean. The poster should be simple, easy to read, and hint at the themes of the film without giving the twist away.

Here is a link to the Fine Cut of the film: https://clipvault.example/48210576 The password is: lanterns72
It is not a completed version but will give you an idea of what the film will look like.

Target Market(s)

The intended audience is an art-film crowd of moviegoers.

Industry/Entity Type

Movie

Requirements
Must have
• The poster must have the typical movie poster text at the bottom. The information that should be included is: First line: COPPER LANTERN STUDIOS presents a film by DANIEL OSTROM "DRIFTWATER" MARCEL BRUNAUD TERRA WOLCOTT
Second line: music by OWEN PRATT director of photography VICTOR L. MORALES edited by SIMON ORR costume designer ROBERTA CLINE
Third line: produced by GAIL TORVALD DANIEL OSTROM written and directed by DANIEL OSTROM

It should have the title of the film "Driftwater" and "A film by Daniel Ostrom" on the poster (in addition to the text at the bottom.

It must be high-quality and printable to a size of 20x30. Ideal resolution is 6060x9090. I only need the high quality printable file, I will do the printing myself.
Should not have
• Bright colors.

```html
<!DOCTYPE html>
<html lang="en">
<head>
<meta charset="utf-8">
<title>Driftwater — A film by Daniel Ostrom</title>
<link rel="stylesheet" href="https://fonts.googleapis.com/css2?family=Questrial&display=swap">
<style>
  :root {
    --ink-deep: #1c1c1c;
    --ink-mid: #3a3a3a;
    --haze: #8a8a8a;
    --field: #4a4a4a;
    --title: #ffffff;
    --credit-name: #f2f2f2;
    --credit-role: #9a9a9a;
  }
  html, body {
    margin: 0;
    padding: 0;
    width: 800px;
    height: 1200px;
    overflow: hidden;
    background: var(--ink-deep);
  }
  .poster {
    position: relative;
    width: 800px;
    height: 1200px;
    overflow: hidden;
    font-family: "Questrial", "Century Gothic", sans-serif;
  }
  .poster__scene {
    position: absolute;
    inset: 0;
    width: 800px;
    height: 1200px;
  }
  .poster__title {
    position: absolute;
    left: 114px;
    top: 652px;
    margin: 0;
    font-weight: 400;
    font-size: 86px;
    line-height: 1;
    letter-spacing: 0.005em;
    color: var(--title);
  }
  .poster__byline {
    position: absolute;
    left: 118px;
    top: 756px;
    margin: 0;
    font-size: 22px;
    color: var(--title);
  }
  .credits {
    position: absolute;
    left: 0;
    right: 0;
    top: 1060px;
    margin: 0;
    padding: 0;
    list-style: none;
    text-align: center;
    font-size: 16.5px;
    line-height: 20px;
    text-transform: uppercase;
    color: var(--credit-name);
    white-space: nowrap;
  }
  .credits .role {
    color: var(--credit-role);
    text-transform: none;
  }
  .credits .gap { margin-left: 0.9em; }
</style>
</head>
<body>
<main class="poster">
  <svg class="poster__scene" viewBox="0 0 800 1200" role="img" aria-label="Weathered black-and-white photograph: a lone man seen from behind, hand to his head, standing in an empty field beneath a crossroads signpost under a misty sky">
    <defs>
      <linearGradient id="sky-field" x1="0" y1="0" x2="0" y2="1">
        <stop offset="0" stop-color="#2a2a2a"/>
        <stop offset="0.12" stop-color="#5a5a5a"/>
        <stop offset="0.24" stop-color="#8c8c8c"/>
        <stop offset="0.33" stop-color="#7a7a7a"/>
        <stop offset="0.345" stop-color="#4c4c4c"/>
        <stop offset="0.55" stop-color="#505050"/>
        <stop offset="0.8" stop-color="#3e3e3e"/>
        <stop offset="1" stop-color="#2e2e2e"/>
      </linearGradient>
      <radialGradient id="vignette" cx="0.5" cy="0.42" r="0.75">
        <stop offset="0.45" stop-color="#000" stop-opacity="0"/>
        <stop offset="1" stop-color="#000" stop-opacity="0.6"/>
      </radialGradient>
    </defs>
    <rect width="800" height="1200" fill="url(#sky-field)"/>
    <rect width="800" height="1200" fill="url(#vignette)"/>
  </svg>

  <h1 class="poster__title">DRIFTWATER</h1>
  <p class="poster__byline">A film by Daniel Ostrom</p>

  <ul class="credits">
    <li>COPPER LANTERN STUDIOS <span class="role">presents a film by</span> DANIEL OSTROM <span class="role">"</span>DRIFTWATER<span class="role">"</span></li>
    <li>MARCEL BRUNAUD<span class="gap"></span>TERRA WOLCOTT</li>
    <li><span class="role">music by</span> OWEN PRATT<span class="gap"></span><span class="role">director of photography</span> VICTOR L. MORALES</li>
    <li><span class="role">edited by</span> SIMON ORR<span class="gap"></span><span class="role">costume designer</span> ROBERTA CLINE</li>
    <li><span class="role">produced by</span> GAIL TORVALD DANIEL OSTROM <span class="role">written and directed by</span> DANIEL OSTROM</li>
  </ul>
</main>
</body>
</html>
```